Vantor Advisory business card

Premium business card required
I have attached the brand as a powerpoint template but this can be made to look very up market, I have also attached my BIO for title reasons and to give you a feel for my skills
front of card
Derek Holloway
Managing Director Vantor Advisory
Retail, Customer-Led Experience, Transformation and Maximising Shareholder Return
Mobile +61(0)418557392
Email derekvantoradvisory.com
back of card

VANTOR ADVISORY’ OFFERING

We transform customer environments to extract benefits while elevating service levels;
We release millions of dollars in self-funding through continuous improvement;
We see CX as a key differentiator, proactively guarding share from market disrupters;
We re-invent service and create front-end of the future.

```html
<!DOCTYPE html>
<html lang="en">
<head>
<meta charset="utf-8">
<title>Vantor Advisory business card</title>
<link href="https://fonts.googleapis.com/css2?family=Montserrat:wght@400;500;700;800&display=swap" rel="stylesheet">
<style>
  :root {
    --ink: #555555;
    --charcoal: #5a5a5a;
    --gold: #c9b14f;
    --paper: #ffffff;
    --edge: #1a1a1a;
  }
  html, body {
    margin: 0;
    padding: 0;
    width: 1200px;
    height: 1000px;
    overflow: hidden;
    background: var(--paper);
    font-family: "Montserrat", Arial, sans-serif;
  }
  .canvas {
    position: relative;
    width: 1200px;
    height: 1000px;
  }
  .card {
    position: absolute;
    top: 380px;
    width: 400px;
    height: 240px;
    box-sizing: border-box;
    overflow: hidden;
  }
  /* Front */
  .card-front {
    left: 182px;
    background: var(--paper);
    border: 1px solid var(--edge);
  }
  .front-brand {
    position: absolute;
    top: 26px;
    right: 24px;
    display: flex;
    align-items: center;
    gap: 6px;
    font-weight: 800;
    font-size: 22px;
    letter-spacing: 0.5px;
    color: var(--ink);
    line-height: 1;
  }
  .front-brand .mark {
    width: 16px;
    height: 16px;
    background: var(--gold);
  }
  .contact {
    position: absolute;
    left: 25px;
    top: 110px;
    color: var(--ink);
  }
  .contact .name {
    margin: 0;
    font-size: 14px;
    font-weight: 700;
    line-height: 17px;
  }
  .contact .role {
    margin: 0 0 8px;
    font-size: 10.5px;
    line-height: 13px;
  }
  .contact .line {
    margin: 0;
    font-size: 10.5px;
    line-height: 14px;
  }
  .tagline {
    position: absolute;
    left: 0;
    right: 0;
    bottom: 0;
    height: 30px;
    background: var(--gold);
    color: var(--paper);
    font-size: 7.6px;
    display: flex;
    align-items: center;
    justify-content: center;
    white-space: nowrap;
  }
  /* Back */
  .card-back {
    left: 619px;
    width: 398px;
    background: var(--charcoal);
  }
  .stripe {
    position: absolute;
    left: 0;
    right: 0;
    height: 6px;
    background: var(--gold);
  }
  .stripe-top { top: 25px; }
  .stripe-bottom { top: 205px; }
  .back-brand {
    position: absolute;
    left: 0;
    right: 0;
    top: 72px;
    display: flex;
    align-items: center;
    justify-content: center;
    gap: 12px;
    color: var(--paper);
    font-weight: 800;
  }
  .back-brand .mark {
    width: 40px;
    height: 40px;
    background: var(--gold);
  }
  .back-brand .wordmark {
    display: flex;
    flex-direction: column;
    align-items: center;
    line-height: 1;
  }
  .back-brand .word-main {
    font-size: 50px;
    letter-spacing: 1px;
  }
  .back-brand .word-sub {
    font-size: 15px;
    letter-spacing: 4.5px;
    margin-top: 6px;
  }
</style>
</head>
<body>
<main class="canvas">
  <section class="card card-front" aria-label="Business card front">
    <div class="front-brand"><span class="brand-name">VANTOR</span><span class="mark"></span></div>
    <div class="contact">
      <p class="name">Derek Holloway</p>
      <p class="role">Managing Director Vantor Advisory</p>
      <p class="line">Mobile +61(0)418557392</p>
      <p class="line">Email: derekvantoradvisory.com</p>
    </div>
    <div class="tagline">Retail | Customer-Led Experience | Transformation and Maximising Shareholder Return</div>
  </section>

  <section class="card card-back" aria-label="Business card back">
    <div class="stripe stripe-top"></div>
    <div class="back-brand">
      <div class="wordmark">
        <span class="word-main">VANTOR</span>
        <span class="word-sub">ADVISORY</span>
      </div>
      <span class="mark"></span>
    </div>
    <div class="stripe stripe-bottom"></div>
  </section>
</main>
</body>
</html>
```